Lanternfield Billboard - Financial Services Company (Investments, Tax Planning and Insurance)

Our new office has a billboard directly above the office building. We'd like something eye-catching with a strong Call to Action, with the main part of the billboard being under 7 words if possible. We'd like you to include a way to get ahold of us (either our website lanternfieldllc.example or our phone number 302-418-2967. You may also include in small font something to indicate that we've been serving the area since 1980 (the DE area, the tri-state area, the Copperleaf Basin, etc.)

We offer financial planning, tax planning, and insurance, and we help our clients to focus on their goals and happiness by providing everything they need for lifelong wealth under one roof.

Our logos are attached, we use a triangle logo with green and gray. We use the tagline "experience lifelong wealth" but this does not need to be included.

Potential ideas we have seen from other financial companies-
- the concept that the driver spends more time looking at billboards than planning for their retirement
-something along the lines of "everything you need for your finances is in this building right here" planning, investments, taxes, insurance"
-don't spend your time worrying about retirement, let us help you plan for it
-are you working for your money, or is it working for you?
- retirement takes planning, we're here to help
- ready to retire? talk to us
- need investment advice?
- need help investing?
- crossing your fingers isn't a retirement plan. we can help.
- retiring soon? you need help.

Those are just general ideas, please feel free to be creative.

brand colors:
#00b585
#00b185
#000000
#ffffff
#6d6f75
#6d6f75
#6f7074
#021712
#052e24

```html
<!DOCTYPE html>
<html lang="en">
<head>
<meta charset="utf-8">
<title>Lanternfield Billboard</title>
<link rel="stylesheet" href="https://fonts.googleapis.com/css2?family=Lora:wght@700&family=Oswald:wght@700&family=Poppins:wght@400;700;800&display=swap">
<style>
  :root {
    --page-bg: #b2b2b2;
    --board-bg: #ffffff;
    --brand-green: #009a66;
    --brand-gray: #6d6f75;
    --ink: #111111;
    --diamond: #c4c4c4;
    --white: #ffffff;
  }
  * { margin: 0; padding: 0; box-sizing: border-box; }
  html, body {
    width: 1200px; height: 1200px; overflow: hidden;
    background: var(--page-bg);
  }
  .billboard {
    position: absolute; left: 58px; top: 345px;
    width: 1084px; height: 514px;
    background: var(--board-bg);
    overflow: hidden;
  }
  .photo-area {
    position: absolute; right: 0; top: 0;
    width: 640px; height: 100%;
    background: linear-gradient(90deg, rgba(255,255,255,1) 0%, rgba(240,232,215,0.6) 25%, #d9c4a0 50%, #8a5a3e 65%, #c9a98a 80%, #d88e9a 100%);
  }
  .brand {
    position: absolute; left: 37px; top: 42px;
    display: flex; align-items: center; gap: 18px;
  }
  .brand-square {
    width: 52px; height: 52px; background: var(--brand-green);
  }
  .brand-name {
    font-family: "Lora", serif; font-weight: 700;
    font-size: 58px; line-height: 1; color: var(--brand-green);
  }
  .headline-lead {
    position: absolute; left: 30px; top: 140px;
    font-family: "Lora", serif; font-weight: 700;
    font-size: 32px; color: var(--brand-gray); white-space: nowrap;
  }
  .headline-lead .accent { color: var(--brand-green); }
  .headline-mid {
    position: absolute; left: 28px; top: 180px;
    font-family: "Poppins", sans-serif; font-weight: 700;
    font-size: 74px; line-height: 1.2; letter-spacing: -2px;
    color: var(--brand-gray); white-space: nowrap;
  }
  .headline-main {
    position: absolute; left: 24px; top: 254px;
    font-family: "Poppins", sans-serif; font-weight: 800;
    font-size: 128px; line-height: 1.2; letter-spacing: -3px;
    color: var(--brand-green); white-space: nowrap;
  }
  .divider {
    position: absolute; left: 246px; top: 391px;
    display: flex; gap: 6px;
  }
  .divider span {
    width: 12px; height: 12px; background: var(--diamond);
    transform: rotate(45deg);
  }
  .services-intro {
    position: absolute; left: 33px; top: 421px;
    font-family: "Poppins", sans-serif; font-weight: 400;
    font-size: 17.5px; color: var(--ink); white-space: nowrap;
  }
  .services-list {
    position: absolute; left: 32px; top: 447px;
    font-family: "Poppins", sans-serif; font-weight: 400;
    font-size: 28px; color: var(--ink); white-space: nowrap;
  }
  .call-arrow {
    position: absolute; left: 655px; top: 383px;
    width: 429px; height: 130px;
  }
  .arrow-shape { position: absolute; left: 0; top: 0; }
  .phone-icon {
    position: absolute; left: 36px; top: 42px; width: 46px; height: 46px;
  }
  .phone-number {
    position: absolute; right: 18px; top: 22px;
    font-family: "Oswald", sans-serif; font-weight: 700;
    font-size: 58px; line-height: 86px; color: var(--white);
    white-space: nowrap;
  }
</style>
</head>
<body>
  <div class="billboard">
    <div class="photo-area" role="img" aria-label="Photo of a smiling older couple reviewing their finances together at home"></div>

    <div class="brand">
      <div class="brand-square"></div>
      <div class="brand-name">Lanternfield</div>
    </div>

    <p class="headline-lead">are you working for <span class="accent">your money?</span></p>
    <p class="headline-mid">or is it working</p>
    <p class="headline-main">FOR YOU?</p>

    <div class="divider"><span></span><span></span><span></span><span></span><span></span><span></span><span></span><span></span></div>

    <p class="services-intro">everything you need for your finances is in this building right here</p>
    <p class="services-list">planning • investments, • taxes, • insurance</p>

    <div class="call-arrow">
      <svg class="arrow-shape" viewBox="0 0 429 130" width="429" height="130" aria-hidden="true">
        <polygon points="0,65 78,0 78,22 429,22 429,108 78,108 78,130" fill="#009a66"/>
      </svg>
      <svg class="phone-icon" viewBox="0 0 24 24" aria-hidden="true">
        <path fill="#fff" d="M6.6 10.8c1.4 2.8 3.8 5.1 6.6 6.6l2.2-2.2c.3-.3.7-.4 1-.2 1.1.4 2.300.6 3.6.6.6 0 1 .4 1 1V20c0 .6-.4 1-1 1C10.6 21 3 13.4 3 4c0-.6.4-1 1-1h3.5c.6 0 1 .4 1 1 0 1.3.2 2.5.6 3.6.1.3 0 .7-.2 1L6.6 10.8z"/>
        <path fill="none" stroke="#fff" stroke-width="1.6" stroke-linecap="round" d="M14 3.5a7 7 0 0 1 6.5 6.5M14 7a3.5 3.5 0 0 1 3 3"/>
      </svg>
      <div class="phone-number">302-418-2967</div>
    </div>
  </div>
</body>
</html>
```